Ridgeway Moss - Facebook Cover Photo & Photo Icon Design

We’re looking for a Facebook Cover Photo and Profile Icon design for Ridgeway Moss, a leading Residential Real Estate brand under Ridgeway Property Agents, based in Capalaba and Alexandra Hills, Queensland, Australia.

This design will represent my professional real estate profile and needs to be bold, clean, and on-brand.

Deliverables:

Facebook Cover Photo (820 x 312 px, optimized for mobile + desktop)

Facebook Profile Icon (1:1 ratio, minimum 320 x 320 px)

Design Guidelines:

1. Must Include:

The Ridgeway Moss logo (provided after project start)

Use of the Ridgeway Property Agents brand colour palette (will be supplied)

Clear connection to residential real estate

2. Optional but Preferred:

A local photo or skyline of Capalaba or Alexandra Hills in QLD (bonus points for this)

Space for a short tagline like:
“Selling Faster. Selling Smarter. Selling Ridgeway.”
(Optional tagline – open to variations if it improves layout/design)

3. Style & Feel:

Professional yet personable

Clean, modern aesthetic

Subtle touches of fun or personality are welcome

Layout must work well when overlaid by Facebook UI elements (like profile photo & call-to-action buttons)

Who I Am:
I'm a well-known residential real estate agent in the Redlands area, known for high-energy campaigns, premium video marketing, and a results-driven approach. My brand is fun, fresh, and high-performing — just like the real estate campaigns I run.

Files to be Provided (after selection):

Ridgeway Moss logo in high-res

Brand colour palette / style reference

Optional photo references if local imagery is not sourced by designer

Final Notes:

Make sure all text is legible on mobile and desktop

Original, layered design files must be delivered (PSD or AI preferred)

Bonus points if it feels uniquely “Bayside Queensland” while maintaining a national-level professional polish

Target Market(s)

Alexandra Hills, Capalaba & Sheldon

Industry/Entity Type

Real Estate

Colors
0054AA
0677BA
7BADD7
CADEEF
E8F1F8

Requirements
Must have
• Headshot, Mobile Number 0491 726 805, Suburbs - Alexandra Hills, Capalaba & Sheldon
Nice to have
• White, Crisp & Professional. Bottom Banner with Suburb List. Specialising in Alexandra Hills, Capalaba & Sheldon

```html
<!DOCTYPE html>
<html lang="en">
<head>
<meta charset="utf-8">
<title>Ridgeway Moss – Facebook Cover</title>
<link rel="stylesheet" href="https://fonts.googleapis.com/css2?family=Josefin+Sans:wght@300&family=Source+Sans+3:ital,wght@0,400;1,700&family=Poppins:wght@400&display=swap">
<style>
  :root {
    --page-bg: #a3a3a3;
    --navy: #05124f;
    --navy-deep: #030b3c;
    --gold: #d4a26a;
    --gold-dark: #a87b4c;
    --white: #ffffff;
    --silver: #d9dce2;
    --base-strip: #26282a;
  }
  * { margin: 0; padding: 0; box-sizing: border-box; }
  html, body {
    width: 1140px; height: 1200px; overflow: hidden;
    background: var(--page-bg);
  }
  .cover {
    position: absolute;
    left: 30px; top: 400px;
    width: 1080px; height: 399px;
    background: linear-gradient(180deg, var(--navy) 0%, var(--navy-deep) 100%);
    overflow: hidden;
  }
  .cover-art { position: absolute; inset: 0; width: 1080px; height: 399px; }
  .base-strip {
    position: absolute; left: 0; bottom: 0; width: 100%; height: 11px;
    background: var(--base-strip);
  }
  .brand-name {
    position: absolute; left: 60px; top: 40px; width: 440px;
    text-align: center;
    font-family: "Josefin Sans", sans-serif; font-weight: 300;
    color: var(--white);
    line-height: 1;
  }
  .brand-name .first { display: block; font-size: 44px; letter-spacing: 4px; }
  .brand-name .second { display: block; font-size: 100px; letter-spacing: 6px; margin-top: 6px; }
  .tagline {
    position: absolute; left: 40px; top: 198px; width: 450px;
    text-align: center;
    font-family: "Source Sans 3", sans-serif; font-size: 20px;
    color: var(--white); white-space: nowrap;
  }
  .tagline em { font-style: italic; font-weight: 700; color: var(--gold); }
  .web-pill {
    position: absolute; left: 129px; top: 263px;
    width: 330px; height: 46px; border-radius: 6px;
    background: linear-gradient(90deg, var(--gold) 0%, #6e5a5a 45%, var(--navy-deep) 100%);
    display: flex; align-items: center; gap: 8px; padding-left: 12px;
    font-family: "Poppins", sans-serif; font-size: 16px; color: var(--white);
  }
  .web-pill svg { width: 20px; height: 20px; flex: none; }
</style>
</head>
<body>
  <section class="cover">
    <svg class="cover-art" viewBox="0 0 1080 399" aria-hidden="false">
      <defs>
        <linearGradient id="poolPhoto" x1="0" y1="0" x2="0" y2="1">
          <stop offset="0" stop-color="#7cc3f0"/>
          <stop offset="0.4" stop-color="#8a8f95"/>
          <stop offset="0.65" stop-color="#5fc9c4"/>
          <stop offset="1" stop-color="#9a9da0"/>
        </linearGradient>
        <linearGradient id="patioPhoto" x1="0" y1="0" x2="0" y2="1">
          <stop offset="0" stop-color="#e6e6e8"/>
          <stop offset="0.4" stop-color="#6f6c68"/>
          <stop offset="0.7" stop-color="#b9a48c"/>
          <stop offset="1" stop-color="#6d6f78"/>
        </linearGradient>
        <linearGradient id="gardenPhoto" x1="0" y1="0" x2="0" y2="1">
          <stop offset="0" stop-color="#7fbff0"/>
          <stop offset="0.35" stop-color="#6d8a4d"/>
          <stop offset="0.7" stop-color="#6e6a62"/>
          <stop offset="1" stop-color="#4fa33a"/>
        </linearGradient>
        <linearGradient id="goldSwoosh" x1="0" y1="1" x2="0.6" y2="0">
          <stop offset="0" stop-color="#c9965e"/>
          <stop offset="1" stop-color="#2a2a55"/>
        </linearGradient>
      </defs>

      <polygon class="photo photo-pool" role="img" aria-label="Photo of a backyard swimming pool beside a single-storey home"
               points="648,0 809,0 726,351 566,351" fill="url(#poolPhoto)"/>
      <polygon class="photo photo-patio" role="img" aria-label="Photo of a covered outdoor patio with lounge chairs and barbecue"
               points="809,29 971,29 885,388 726,388" fill="url(#patioPhoto)"/>
      <polygon class="photo photo-garden" role="img" aria-label="Photo of a brick home with a green lawn and rock garden"
               points="987,0 1080,0 1080,290 1064,351 904,351" fill="url(#gardenPhoto)"/>

      <path class="gold-swoosh" d="M553,388 C600,380 640,360 640,320 C640,270 600,230 618,150 C626,120 650,105 690,108 C660,130 650,160 660,210 C668,260 650,330 638,388 Z"
            fill="url(#goldSwoosh)"/>
      <path class="silver-line" d="M822,9 C760,40 700,20 620,30 C560,38 560,90 578,150 C600,220 620,280 560,320 C510,350 450,365 404,388"
            fill="none" stroke="var(--silver)" stroke-width="2.5"/>
    </svg>

    <h1 class="brand-name"><span class="first">RIDGEWAY</span><span class="second">MOSS</span></h1>

    <p class="tagline">“Selling Faster. Selling Smarter. Selling <em>Ridgeway</em>.”</p>

    <div class="web-pill">
      <svg viewBox="0 0 24 24" fill="none" stroke="#ffffff" stroke-width="1.4">
        <circle cx="12" cy="12" r="10"/>
        <ellipse cx="12" cy="12" rx="4.5" ry="10"/>
        <line x1="2" y1="12" x2="22" y2="12"/>
        <path d="M4 7h16M4 17h16"/>
      </svg>
      <span class="web-address">ridgewaypropertyagents.com.au</span>
    </div>

    <div class="base-strip"></div>
  </section>
</body>
</html>
```